An international wholesale business needs letterhead design

Logo file is attached. Please design a letterhead with the following details:

- Company Name and Logo
- Address
- VAT Registration number
- Phone No
- Website address

```html
<!DOCTYPE html>
<html lang="en">
<head>
<meta charset="utf-8">
<title>Norvale Trading Letterhead</title>
<link href="https://fonts.googleapis.com/css2?family=Lexend:wght@300;400;600&display=swap" rel="stylesheet">
<style>
  :root {
    --backdrop: #d2d3d5;
    --paper: #ffffff;
    --brand-red: #c1272d;
    --brand-grey: #8a9197;
    --ink: #333538;
    --rule: #bfc2c5;
    --signature-tone: #e9eaec;
  }
  * { margin: 0; padding: 0; box-sizing: border-box; }
  html, body { width: 1200px; height: 1000px; overflow: hidden; }
  body {
    background: var(--backdrop);
    font-family: "Lexend", sans-serif;
    color: var(--ink);
    position: relative;
  }
  .letterhead {
    position: absolute;
    left: 293px; top: 70px;
    width: 614px; height: 860px;
    background: var(--paper);
    overflow: hidden;
  }
  .letterhead > * { position: absolute; }
  .brand { left: 77px; top: 65px; display: flex; align-items: center; gap: 8px; }
  .brand-mark { width: 40px; height: 40px; border-radius: 50%; background: var(--brand-red); }
  .brand-name { font-size: 24px; font-weight: 600; color: var(--brand-red); letter-spacing: 0.5px; }
  .contact-divider { left: 413px; top: 60px; width: 1.5px; height: 52px; background: var(--rule); }
  .contact-list { left: 428px; top: 65px; list-style: none; font-size: 10.5px; line-height: 14px; font-weight: 300; }
  .contact-list li { display: flex; align-items: center; gap: 5px; }
  .contact-list svg { width: 10px; height: 10px; }
  .recipient-label { left: 80px; top: 168px; font-size: 13.5px; }
  .person-name { font-size: 14.5px; font-weight: 600; line-height: 14px; }
  .recipient-name { left: 80px; top: 188px; }
  .recipient-details { left: 80px; top: 225px; font-size: 12px; line-height: 16px; font-weight: 300; }
  .recipient-details b { font-weight: 600; }
  .letter-date { right: 78px; top: 273px; font-size: 12px; font-weight: 300; }
  .letter-date b { font-weight: 600; }
  .salutation { left: 80px; top: 294px; font-size: 12px; font-weight: 300; }
  .letter-body { left: 80px; top: 319px; width: 460px; font-size: 12.4px; line-height: 16px; font-weight: 300; }
  .letter-body p + p { margin-top: 16px; }
  .closing { left: 79px; top: 581px; font-size: 12px; font-weight: 300; }
  .signature { left: 79px; top: 606px; width: 121px; height: 30px; border-radius: 4px;
    background: linear-gradient(90deg, var(--signature-tone), #f4f4f5); }
  .sender-name { left: 80px; top: 645px; }
  .footer-vat { left: 0; width: 614px; top: 764px; text-align: center; font-size: 10px; font-weight: 300; }
  .footer-rule { left: 80px; top: 780px; width: 454px; height: 1.5px; background: var(--rule); }
  .footer-address { left: 0; width: 614px; top: 786px; font-size: 10px; font-weight: 300;
    display: flex; justify-content: center; align-items: center; gap: 5px; }
  .footer-address svg { width: 11px; height: 11px; }
  .band-grey { left: 0; top: 819px; width: 614px; height: 7px; background: var(--brand-grey); }
  .band-red { left: 0; top: 833px; width: 614px; height: 27px; background: var(--brand-red); }
</style>
</head>
<body>
  <main class="letterhead">
    <div class="brand">
      <span class="brand-mark"></span>
      <span class="brand-name">Norvale Trading</span>
    </div>

    <div class="contact-divider"></div>
    <ul class="contact-list">
      <li>
        <svg viewBox="0 0 10 10"><circle cx="5" cy="5" r="5" fill="var(--brand-red)"/><path d="M3.3 2.6l1 1-.5.6c.3.7.8 1.2 1.5 1.5l.6-.5 1 1-.6.8C4.6 7 3 5.4 2.5 3.2z" fill="#fff"/></svg>
        +01 555 010 20
      </li>
      <li>
        <svg viewBox="0 0 10 10"><circle cx="5" cy="5" r="5" fill="var(--brand-red)"/><rect x="2.6" y="3.2" width="4.8" height="3.6" rx=".4" fill="#fff"/><path d="M2.8 3.5L5 5.2l2.2-1.7" stroke="var(--brand-red)" stroke-width=".6" fill="none"/></svg>
        hello@norvale.com
      </li>
      <li>
        <svg viewBox="0 0 10 10"><circle cx="5" cy="5" r="5" fill="var(--brand-red)"/><circle cx="5" cy="5" r="2.6" stroke="#fff" stroke-width=".6" fill="none"/><path d="M2.4 5h5.2M5 2.4c-1 1.4-1 3.8 0 5.2M5 2.4c1 1.4 1 3.8 0 5.2" stroke="#fff" stroke-width=".5" fill="none"/></svg>
        norvale.com
      </li>
    </ul>

    <p class="recipient-label">To</p>
    <p class="person-name recipient-name">Mrs: Mr. Example<br>Name</p>
    <p class="recipient-details"><b>P:</b> 987654321<br><b>E:</b> example@email.com<br><b>A:</b> Address, City-123</p>
    <p class="letter-date"><b>Date:</b> 01/01/2022</p>

    <p class="salutation">Dear Example Name</p>
    <div class="letter-body">
      <p>Lorem ipsum dolor sit amet, consectetuer adipiscing elit, sed diam nonummy nibh euismod tincidunt ut laoreet dolore magna aliquam erat volutpat. Ut wisi enim ad minim veniam, quis nostrud exerci tation ullamcorper suscipit lobortis nisl ut aliquip ex ea commodo consequat. Duis autem vel eum iriure dolor in hendrerit in vulputate velit esse molestie consequat, vel illum dolore eu feu.</p>
      <p>Lorem ipsum dolor sit amet, consectetuer adipiscing elit, sed diam nonummy nibh euismod tincidunt ut laoreet dolore magna aliquam erat volutpat. Ut wisi enim ad minim veniam, quis nostrud exerci tation ullamcorper suscipit lobortis nisl ut aliquip ex ea commodo consequat. Duis autem vel eum iriure dolor in hendrerit in vulputate velit esse molestie consequat.</p>
      <p>Lorem ipsum dolor sit amet, consectetuer adipiscing elit, sed diam nonummy nibh euismod tincidunt ut laoreet dolore magna aliquam erat volutpat.</p>
    </div>

    <p class="closing">Yours Sincerely</p>
    <div class="signature" role="img" aria-label="Handwritten signature"></div>
    <p class="person-name sender-name">Mrs: Mr. Example<br>Name</p>

    <p class="footer-vat">VAT registration number : 246813579</p>
    <div class="footer-rule"></div>
    <p class="footer-address">
      <svg viewBox="0 0 10 10"><circle cx="5" cy="5" r="5" fill="var(--brand-red)"/><circle cx="5" cy="4.6" r="1.3" fill="#fff"/></svg>
      48 Harbor Lane, Unit 9, State, IL 60601
    </p>

    <div class="band-grey"></div>
    <div class="band-red"></div>
  </main>
</body>
</html>
```